Tarvell Consulting needs a Business Catalogue

We are looking at creating a business catalogue that is used to introduce ourselves and our business as well as the services we offer. We are an HR business that offers assistance with recruitment and selection and all services involved in that area. We don't offer specific products and don't have prices advertised. it would be good to start with an introduction to the business and our history, some staff bios then a framework to discuss business scenarios where we can help. I would prefer white as the main colour on the front/back page with the colours of the logo (attached) to be used throughout the catalogue along with images and other visual improvements. A mall amount of colour should be used throughout and don't want solid colour pages. Prefer what pages that are broken up by coloured designs, images, diagrams heading etc. A 12-page catalogue with different designs I can move around as needed would be good.

Target Market(s)

Education, government, large business with administration staff

Font styles to use
Sans Serif

Requirements
Must have
• Logo colour scheme
• Images, diagrams, tables etc
• Start with company introduction (history, three staff profiles, company values etc)
• Main section will be the description of services and processes offered.
Nice to have
• A range of different visuals to choose from including designs for tables, paragraphs, diagrams, space for photos and other visual elements.

```html
<!DOCTYPE html>
<html lang="en">
<head>
<meta charset="utf-8">
<title>Tarvell Consulting – Business Catalogue</title>
<link href="https://fonts.googleapis.com/css2?family=Montserrat:wght@400;600;700&family=Open+Sans:wght@400;600;700&family=Roboto+Condensed:wght@700&display=swap" rel="stylesheet">
<style>
:root{
  --backdrop:#dcdcdc;
  --paper:#f3f3f3;
  --paper-white:#fdfdfd;
  --ink:#3b3b3b;
  --ink-soft:#8a8a8a;
  --charcoal:#2b2d2f;
  --charcoal-mid:#3a3c3e;
  --blue:#2f7fbd;
  --green:#8cc63f;
  --orange:#e8862a;
  --teal:#3fb8d0;
  --purple:#9b3c93;
  --sky:#9fd6e8;
  --grey-light:#e9eaea;
}
*{margin:0;padding:0;box-sizing:border-box}
html,body{width:1200px;height:1200px;overflow:hidden}
body{background:var(--backdrop);font-family:"Open Sans",sans-serif;color:var(--ink);position:relative}
.page,.spread{position:absolute;overflow:hidden}
.page{background:var(--paper-white)}
.spread{background:var(--paper)}
.spread .gutter{position:absolute;top:0;bottom:0;width:1px;background:#d6d6d6}
.abs{position:absolute}
.body-copy{font-size:4.4px;line-height:1.6;color:var(--ink-soft);text-align:justify}
.body-copy p+p{margin-top:5px}
.body-copy.light{color:#e6f5fa}
.body-copy.pale{color:#c9c9c9}
.head-cond{font-family:"Roboto Condensed",sans-serif;font-weight:700;letter-spacing:.5px;text-transform:uppercase}
.brand-name{font-family:"Montserrat",sans-serif;font-weight:600;color:var(--charcoal);letter-spacing:.5px}
.brand-row{display:flex;align-items:center;gap:5px}
.brand-mark{width:9px;height:9px;background:var(--green)}
.photo{position:absolute}
/* cover */
.cover .brand-name{font-size:13px}
.cover .brand-sub{font-family:"Montserrat",sans-serif;font-size:5px;letter-spacing:3px;color:var(--ink-soft);margin-top:1px}
/* summary */
.summary-title{font-family:"Montserrat",sans-serif;font-size:17px;color:#b5b5b5;font-weight:600}
.toc{list-style:none}
.toc li{display:flex;align-items:center;height:19px}
.toc .num{font-family:"Montserrat",sans-serif;font-size:12px;color:var(--ink-soft);width:26px}
.toc .item{font-family:"Montserrat",sans-serif;font-size:5.5px;color:var(--ink-soft);letter-spacing:.4px;line-height:1.1}
.icon-ring{position:absolute;width:22px;height:22px;border:1.2px solid var(--blue);border-radius:50%}
/* lists */
.num-list{list-style:none;font-size:4.4px;line-height:1.6;color:var(--ink-soft)}
.num-list li{display:flex;gap:4px;margin-bottom:6px}
.num-list.light{color:#e6f5fa}
.section-head{font-size:6.4px;color:var(--ink)}
.section-head.light{color:#fff}
.rule{border-bottom:.6px solid #bdbdbd;padding-bottom:3px;margin-bottom:5px}
.rule.light{border-color:#d8f0f7}
/* services */
.vol-title{font-family:"Montserrat",sans-serif;font-size:10px;letter-spacing:1px;color:var(--ink)}
.service-head{font-family:"Montserrat",sans-serif;font-size:6.4px;line-height:1;text-transform:uppercase}
.stat{font-family:"Montserrat",sans-serif;text-align:center}
.stat .big{font-size:14px;font-weight:600;line-height:1}
.stat .lbl{font-size:4px;letter-spacing:.4px;text-transform:uppercase}
.stat .sub{font-size:3.4px;color:var(--ink-soft)}
.stat-sep{position:absolute;width:1px;height:18px;background:#8a8a8a}
/* dark spread */
.dark-head{font-family:"Montserrat",sans-serif;font-weight:700;font-size:7.5px;color:#fff;line-height:1.15}
.dark-stat .big{font-family:"Montserrat",sans-serif;font-weight:700;font-size:18px;color:var(--orange);line-height:1}
.dark-stat .lbl{font-family:"Montserrat",sans-serif;font-size:5.6px;color:#fff;font-weight:600}
.dark-stat .sub{font-size:3.8px;color:#ddd}
.dark-sub{font-family:"Open Sans",sans-serif;font-weight:700;font-size:6.4px;color:#fff}
.article-head{font-family:"Montserrat",sans-serif;font-weight:700;font-size:5.8px;line-height:1.2;color:var(--ink)}
.article-head .accent{color:var(--green)}
.caption{position:absolute;left:0;right:0;bottom:0;height:7px;background:#555;color:#eee;font-size:3px;padding:2px 3px}
/* back cover */
.back .brand-name{font-size:10px}
.contact{list-style:none;font-family:"Montserrat",sans-serif;font-size:6.4px;color:var(--ink)}
.contact li{display:flex;gap:6px;align-items:center;margin-bottom:3px;line-height:1.3}
.contact svg{flex:none}
</style>
</head>
<body>

<!-- Front cover -->
<section class="page cover" style="left:175px;top:145px;width:279px;height:279px">
  <svg class="abs" width="279" height="279" viewBox="0 0 279 279" style="left:0;top:0">
    <rect width="279" height="279" fill="var(--paper-white)"/>
    <polygon points="200,279 279,200 279,279" fill="var(--charcoal)"/>
    <polygon points="70,0 90,0 279,189 279,209" fill="var(--blue)"/>
    <polygon points="0,0 40,0 279,239 279,279 240,279 0,40" fill="var(--green)"/>
  </svg>
  <div class="photo" role="img" aria-label="Dotted world map illustration" style="left:95px;top:20px;width:175px;height:120px;background:radial-gradient(ellipse at 55% 45%,rgba(47,127,189,.22),rgba(47,127,189,.07) 60%,rgba(47,127,189,0) 75%)"></div>
  <div class="abs" style="left:43px;top:212px">
    <div class="brand-row"><span class="brand-mark"></span><span class="brand-name">TARVELL</span></div>
    <div class="brand-sub" style="padding-left:14px">CONSULTING</div>
  </div>
</section>

<!-- Introduction & summary spread -->
<section class="spread" style="left:491px;top:144px;width:541px;height:280px">
  <span class="gutter" style="left:270px"></span>
  <div class="photo" role="img" aria-label="Faint dotted world map across the spread" style="left:108px;top:32px;width:242px;height:140px;background:radial-gradient(ellipse at 50% 45%,rgba(170,170,170,.45),rgba(170,170,170,.12) 60%,rgba(170,170,170,0) 75%)"></div>
  <div class="abs" style="left:29px;top:48px;width:136px;border-top:.6px solid #c6c6c6"></div>
  <h2 class="abs head-cond" style="left:29px;top:68px;font-size:9px;color:var(--orange)">You Perfect Brand</h2>
  <div class="abs" style="left:29px;top:84px;width:136px;border-top:.6px solid #c6c6c6"></div>
  <div class="abs body-copy" style="left:29px;top:100px;width:136px">
    <p>Tarvell Consulting began as a small recruitment practice and has grown into a trusted people partner for schools, councils and large organisations across the region.</p>
    <p>We help clients find, select and keep the right administration staff through a clear process, honest advice and a team that stays close from the first brief to the final placement and beyond.</p>
  </div>
  <span class="icon-ring" style="left:48px;top:215px"></span>
  <span class="icon-ring" style="left:84px;top:215px"></span>
  <span class="icon-ring" style="left:121px;top:215px"></span>
  <svg class="abs" width="110" height="22" style="left:48px;top:215px" viewBox="0 0 110 22" fill="none" stroke="var(--blue)" stroke-width="1">
    <circle cx="12" cy="9" r="3"/><line x1="10" y1="12" x2="7" y2="16"/>
    <rect x="44" y="6" width="6" height="3"/><rect x="41" y="13" width="5" height="3"/><rect x="48" y="13" width="5" height="3"/><line x1="47" y1="9" x2="47" y2="13"/>
    <polyline points="77,7 77,16 86,16"/><polyline points="78,14 81,11 83,13 86,9"/>
  </svg>

  <h2 class="abs summary-title" style="left:345px;top:42px">summary</h2>
  <ol class="abs toc" style="left:356px;top:69px">
    <li><span class="num">8</span><span class="item">OUR HISTORY</span></li>
    <li><span class="num">12</span><span class="item">MEET THE TEAM</span></li>
    <li><span class="num">22</span><span class="item">OUR VALUES</span></li>
    <li><span class="num">34</span><span class="item">RECRUITMENT AND<br>SELECTION SERVICES</span></li>
    <li><span class="num">55</span><span class="item">OUR PROCESS</span></li>
    <li><span class="num">80</span><span class="item">CLIENT SCENARIOS</span></li>
    <li><span class="num">98</span><span class="item">CONTACT US</span></li>
  </ol>
</section>

<!-- Values & framework spread -->
<section class="spread" style="left:44px;top:470px;width:542px;height:280px">
  <span class="gutter" style="left:269px"></span>
  <div class="abs" style="left:10px;top:18px;width:259px;height:246px;background:var(--sky)"></div>
  <div class="abs" style="left:26px;top:74px;width:106px">
    <h3 class="head-cond section-head light rule light">Who We Are</h3>
    <div class="body-copy light">
      <p>Founded to make hiring simpler for busy teams, we pair careful screening with a personal touch on every role we fill.</p>
      <p>Our consultants know the public and education sectors and bring that insight to each brief.</p>
      <p>We measure success by the people who stay, grow and thrive long after they join our clients.</p>
    </div>
  </div>
  <div class="abs" style="left:146px;top:74px;width:106px">
    <h3 class="head-cond section-head light rule light">Our Values</h3>
    <ol class="num-list light">
      <li><span>1-</span><span>Integrity in every conversation, with clear advice and open reporting to clients and candidates alike.</span></li>
      <li><span>2-</span><span>Care for people at every stage, from first call to placement.</span></li>
    </ol>
  </div>

  <div class="photo" role="img" aria-label="Photo of a consultant touching a digital network screen" style="left:288px;top:26px;width:96px;height:116px;background:linear-gradient(135deg,#cfe2ef,#6f9dbd 55%,#2f4e6b)"></div>
  <div class="abs" style="left:403px;top:27px;width:108px">
    <h3 class="head-cond section-head rule">Our History</h3>
    <div class="body-copy">
      <p>Our first office opened with two recruiters and a simple promise to listen before we search.</p>
      <p>Over the years we expanded into selection testing, onboarding and workforce planning services.</p>
      <p>Today we support education, government and large business clients with a full hiring service.</p>
    </div>
  </div>
  <div class="abs" style="left:286px;top:168px;width:108px">
    <h3 class="head-cond section-head rule">Our Framework</h3>
    <ol class="num-list">
      <li><span>1-</span><span>Understand the role, team and goals, then agree a clear search plan with the client.</span></li>
      <li><span>2-</span><span>Shortlist, assess and support each hire through to a confident start.</span></li>
    </ol>
  </div>
  <svg class="abs" width="110" height="100" viewBox="0 0 110 100" style="left:402px;top:160px" fill="none" stroke="var(--blue)" stroke-width=".8">
    <circle cx="55" cy="50" r="18"/>
    <g stroke="var(--teal)">
      <line x1="18" y1="12" x2="42" y2="37"/><line x1="55" y1="12" x2="55" y2="32"/><line x1="92" y1="12" x2="68" y2="37"/>
      <line x1="18" y1="50" x2="37" y2="50"/><line x1="92" y1="50" x2="73" y2="50"/>
      <line x1="18" y1="86" x2="42" y2="63"/><line x1="55" y1="86" x2="55" y2="68"/><line x1="92" y1="86" x2="68" y2="63"/>
    </g>
    <g fill="var(--paper)">
      <circle cx="18" cy="12" r="11"/><circle cx="55" cy="12" r="11"/><circle cx="92" cy="12" r="11"/>
      <circle cx="18" cy="50" r="11"/><circle cx="92" cy="50" r="11"/>
      <circle cx="18" cy="86" r="11"/><circle cx="55" cy="86" r="11"/><circle cx="92" cy="86" r="11"/>
    </g>
    <g fill="var(--teal)" stroke="none">
      <rect x="13" y="8" width="10" height="7"/><rect x="50" y="8" width="10" height="7"/><rect x="87" y="8" width="10" height="7"/>
      <rect x="13" y="46" width="10" height="7"/><rect x="87" y="46" width="10" height="7"/>
      <rect x="13" y="82" width="10" height="7"/><rect x="50" y="82" width="10" height="7"/><rect x="87" y="82" width="10" height="7"/>
    </g>
    <text x="55" y="51.5" font-family="Open Sans,sans-serif" font-size="3.4" fill="var(--blue)" stroke="none" text-anchor="middle">OUR SERVICES</text>
  </svg>
</section>

<!-- Services spread -->
<section class="spread" style="left:614px;top:470px;width:540px;height:280px">
  <span class="gutter" style="left:270px"></span>
  <h2 class="abs vol-title" style="left:29px;top:30px">OUR SERVICES</h2>
  <div class="abs" style="left:29px;top:58px;width:185px">
    <h3 class="service-head" style="color:var(--orange)">▸ Recruitment<br>&nbsp;&nbsp;Search</h3>
    <p class="body-copy" style="margin-top:3px;padding-left:4px">We source, screen and present qualified candidates for administration and support roles within agreed timeframes.</p>
  </div>
  <div class="abs" style="left:29px;top:102px;width:72px">
    <h3 class="service-head" style="color:var(--teal)">▸ Selection<br>&nbsp;&nbsp;Testing</h3>
    <p class="body-copy" style="margin-top:3px;padding-left:4px">Skills tests, structured interviews and reference checks that give clear evidence.</p>
  </div>
  <div class="photo" role="img" aria-label="Photo of two colleagues reviewing work at a screen" style="left:104px;top:104px;width:75px;height:43px;background:linear-gradient(120deg,#f1f1f1,#cdb8b5 50%,#8c6f7f)"></div>
  <div class="abs" style="left:29px;top:157px;width:72px">
    <h3 class="service-head" style="color:var(--purple)">▸ Onboarding<br>&nbsp;&nbsp;Support</h3>
    <p class="body-copy" style="margin-top:3px;padding-left:4px">Induction plans and check-ins that help new staff settle in and stay.</p>
  </div>
  <div class="photo" role="img" aria-label="Photo of printed charts and reports on a desk" style="left:104px;top:159px;width:75px;height:44px;background:linear-gradient(150deg,#e8eef2,#b7c9d4 50%,#6e8aa0)"></div>
  <div class="abs stat" style="left:32px;top:221px;width:32px;color:var(--teal)"><div class="big">433</div><div class="lbl">Placed</div><div class="sub">roles filled</div></div>
  <span class="stat-sep" style="left:71px;top:223px"></span>
  <div class="abs stat" style="left:79px;top:221px;width:32px;color:var(--green)"><div class="big">122</div><div class="lbl">Clients</div><div class="sub">served yearly</div></div>
  <span class="stat-sep" style="left:118px;top:223px"></span>
  <div class="abs stat" style="left:127px;top:221px;width:32px;color:var(--purple)"><div class="big">545</div><div class="lbl">Assessed</div><div class="sub">candidates</div></div>
  <div class="photo" role="img" aria-label="Photo of paper figures holding hands in a circle" style="left:309px;top:34px;width:186px;height:206px;background:linear-gradient(160deg,#e4e7e6,#b9bfbd 55%,#8e9694)"></div>
</section>

<!-- Team & scenario spread -->
<section class="spread" style="left:176px;top:804px;width:540px;height:282px">
  <div class="abs" style="left:14px;top:0;width:255px;height:282px;background:var(--charcoal-mid)"></div>
  <div class="photo" role="img" aria-label="Photo of a hand writing with a pen, softly blurred" style="left:14px;top:100px;width:255px;height:182px;background:linear-gradient(170deg,rgba(58,60,62,1) 0%,#3d4a4f 40%,#1f3036 100%)"></div>
  <h2 class="abs dark-head" style="left:39px;top:26px">MEET OUR TEAM<br>OF HR SPECIALISTS</h2>
  <div class="abs dark-stat" style="left:39px;top:54px"><div class="big">48</div><div class="lbl">CONSULTANTS</div><div class="sub">ACROSS OFFICES</div></div>
  <div class="abs dark-stat" style="left:101px;top:54px"><div class="big">12</div><div class="lbl">YEARS</div><div class="sub">IN BUSINESS</div></div>
  <div class="abs dark-stat" style="left:154px;top:54px"><div class="big">143</div><div class="lbl">PROJECTS</div><div class="sub">THIS YEAR</div></div>
  <h3 class="abs dark-sub" style="left:58px;top:97px">Leadership profiles</h3>
  <div class="abs body-copy pale" style="left:58px;top:108px;width:58px;text-align:left">Our director leads client strategy and brings long experience in public sector hiring, with a focus on fair and transparent selection for every role.</div>
  <div class="abs body-copy pale" style="left:120px;top:108px;width:58px;text-align:left">Our senior consultant manages education clients and coaches hiring panels on structured interviews and clear scoring.</div>
  <h3 class="abs dark-sub" style="left:58px;top:175px">Candidate care</h3>
  <div class="abs body-copy pale" style="left:58px;top:186px;width:58px;text-align:left">Our candidate manager keeps every applicant informed, gives honest feedback and prepares new starters for their first week on site.</div>
  <div class="abs body-copy pale" style="left:120px;top:186px;width:58px;text-align:left">We follow up at one, three and six months so clients and staff feel supported.</div>

  <div class="abs" style="left:432px;top:18px;font-size:3px;color:#777">Tarvell Consulting business catalogue</div>
  <h3 class="abs article-head" style="left:310px;top:46px">▸ WORKING WITH US :<br><span class="accent">&nbsp;&nbsp;A HIRING</span> SCENARIO</h3>
  <div class="abs body-copy" style="left:313px;top:64px;width:101px">
    <p>A regional council needed ten administration officers in six weeks. We met the managers, agreed a profile and built a short, clear campaign.</p>
    <p>Applicants completed a skills test online before a structured interview with the panel.</p>
    <p>We checked references within two days and kept every candidate informed.</p>
    <p>All ten roles were filled on time, and nine staff remained after the first year.</p>
    <p>The council now uses our framework for every new hiring round.</p>
  </div>
  <div class="photo" role="img" aria-label="Photo of a business team standing together" style="left:425px;top:64px;width:39px;height:62px;background:linear-gradient(180deg,#eef0f2,#9aa6b3 60%,#4e5a68)"><span class="caption">Team photo</span></div>
  <div class="photo" role="img" aria-label="Portrait photo of a smiling staff member" style="left:425px;top:134px;width:39px;height:62px;background:linear-gradient(180deg,#f2f2f2,#b9c4d2 60%,#6d82a2)"><span class="caption">Staff profile</span></div>
  <div class="abs" style="left:500px;top:270px;width:10px;height:1.5px;background:var(--green)"></div>
</section>

<!-- Back cover -->
<section class="page back" style="left:754px;top:802px;width:278px;height:278px">
  <svg class="abs" width="278" height="278" viewBox="0 0 278 278" style="left:0;top:0">
    <rect width="278" height="278" fill="var(--paper-white)"/>
    <polygon points="0,0 170,0 0,150" fill="var(--grey-light)"/>
    <polygon points="198,0 234,0 0,206 0,174" fill="var(--green)"/>
    <polygon points="278,225 278,278 225,278" fill="var(--charcoal)"/>
  </svg>
  <div class="abs brand-row" style="left:146px;top:168px"><span class="brand-mark"></span><span class="brand-name">TARVELL</span></div>
  <ul class="abs contact" style="left:146px;top:194px">
    <li><svg width="10" height="10" viewBox="0 0 10 10" fill="none" stroke="#3b3b3b" stroke-width=".8"><circle cx="5" cy="5" r="4.5"/><rect x="3.6" y="2.6" width="2.8" height="4.8" rx=".5"/></svg><span>+65 5550 1842<br>+65 5550 1843</span></li>
    <li><svg width="10" height="10" viewBox="0 0 10 10" fill="none" stroke="#3b3b3b" stroke-width=".8"><circle cx="5" cy="5" r="4.5"/><line x1="3" y1="7" x2="7" y2="3"/></svg><span>hello@tarvell.example<br>tarvell.example</span></li>
    <li><svg width="10" height="10" viewBox="0 0 10 10" fill="none" stroke="#3b3b3b" stroke-width=".8"><circle cx="5" cy="5" r="4.5"/><path d="M5 7.5 C3.5 5.5 3.3 4.8 3.3 4.2 A1.7 1.7 0 0 1 6.7 4.2 C6.7 4.8 6.5 5.5 5 7.5Z"/></svg><span>18 Harlow Street<br>Singapore, 4410</span></li>
  </ul>
</section>

</body>
</html>
```